Youtube Graphic Design for Fitness Brand

I own a personal training/fitness brand called Brisk Harbor Fitness. I am starting my YouTube channel and need artwork for my banner and an animated intro/outro. For my banner, I would like to see designs that incorporate my brand logo and one of the attached images of me. The point of my channel is to help educate others and help them achieve their fitness goals to live happy balanced lives. The final design should present a high quality fitness brand that offers value to its subscribers. I'd like to keep the project with either a predominately black or white color. Not sure if I have a preference on either color being the dominant color.

Target Market(s)

People looking for help with fitness/healthy lifestyle.

Industry/Entity Type

Fitness

Requirements
Must have
• My logo
Nice to have
• One of the attached photos of me

```html
<!DOCTYPE html>
<html lang="en">
<head>
<meta charset="utf-8">
<title>Brisk Harbor Fitness – Channel Banner</title>
<link rel="stylesheet" href="https://fonts.googleapis.com/css2?family=Open+Sans:wght@700&family=Raleway:wght@600;700&display=swap">
<style>
  :root {
    --paper: #efeceb;
    --band: #ffffff;
    --ink: #111111;
    --accent: #e3000f;
    --icon: #262626;
    --photo-warm: #d8b3a0;
    --photo-deep: #c98a72;
  }
  * { margin: 0; padding: 0; box-sizing: border-box; }
  html, body { width: 1200px; height: 675px; overflow: hidden; background: var(--paper); }
  .banner { position: relative; width: 1200px; height: 675px; background: var(--paper); }
  .band {
    position: absolute; left: 0; top: 238px; width: 1200px; height: 198px;
    background: var(--band);
    box-shadow: 0 18px 22px -6px rgba(0,0,0,0.45);
  }
  .subscribe {
    position: absolute; left: 234px; top: 337px;
    transform: translate(-50%, -50%) rotate(-90deg);
    font-family: "Open Sans", Arial, sans-serif; font-weight: 700;
    font-size: 24px; letter-spacing: 0.5px; color: var(--accent); white-space: nowrap;
  }
  .frame {
    position: absolute; left: 268px; top: 265px; width: 553px; height: 145px;
    border: 2.5px solid var(--ink);
  }
  .brand-mark {
    position: absolute; left: 304px; top: 293px; width: 88px; height: 88px;
    border: 4px solid var(--ink); border-radius: 50%;
  }
  .brand-name {
    position: absolute; left: 410px; top: 319px; width: 246px;
    font-family: "Raleway", Arial, sans-serif; font-weight: 700; color: var(--ink);
    text-align: center;
  }
  .brand-name .primary {
    display: block; font-size: 24px; letter-spacing: 5px; line-height: 1;
    white-space: nowrap; margin-right: -5px;
  }
  .brand-name .secondary {
    display: block; font-size: 12px; letter-spacing: 14px; line-height: 1;
    margin-top: 13px; margin-right: -14px;
  }
  .portrait {
    position: absolute; left: 668px; top: 243px; width: 116px; height: 193px;
    background: linear-gradient(to bottom, var(--photo-warm), var(--photo-deep));
  }
  .socials { position: absolute; left: 845px; top: 284px; list-style: none; }
  .socials li { display: flex; align-items: center; height: 24px; margin-bottom: 18px; }
  .socials .dot { width: 23px; height: 23px; border-radius: 50%; background: var(--icon); flex: none; }
  .socials .label {
    margin-left: 17px; font-family: "Raleway", Arial, sans-serif; font-weight: 600;
    font-size: 18px; color: var(--ink); line-height: 1;
  }
</style>
</head>
<body>
<main class="banner">
  <div class="band"></div>
  <div class="subscribe">SUBSCRIBE</div>
  <div class="frame"></div>
  <div class="brand-mark"></div>
  <div class="brand-name">
    <span class="primary">BRISK HARBOR</span>
    <span class="secondary">FITNESS</span>
  </div>
  <div class="portrait" role="img" aria-label="Photo of the trainer in sunglasses and red shorts"></div>
  <ul class="socials">
    <li><span class="dot"></span><span class="label">friendbook</span></li>
    <li><span class="dot"></span><span class="label">chirper</span></li>
    <li><span class="dot"></span><span class="label">snapgram</span></li>
  </ul>
</main>
</body>
</html>
```